VORL Pty Ltd Business Card

Looking for a simple yet eye-catching double-sided business card design using my company logo on one side and contact details on the other.

Target Market(s)

Government

Industry/Entity Type

Communication Systems Engineering

Contact Information for Business Card

VORL Pty Ltd

Requirements
Nice to have
• Would be great to have a QR code so details can be scanned into contacts

```html
<!DOCTYPE html>
<html lang="en">
<head>
<meta charset="utf-8">
<title>VORL Pty Ltd Business Card</title>
<link href="https://fonts.googleapis.com/css2?family=Montserrat:wght@400;500;700;800&display=swap" rel="stylesheet">
<style>
  :root {
    --stage: #2b2e31;
    --card-white: #ffffff;
    --slate: #37424a;
    --slate-light: #4a565e;
    --ink: #2f383e;
    --muted: #6b7378;
    --trace-faint: #e4e6e8;
    --trace-mid: #d3d6d9;
  }
  * { box-sizing: border-box; margin: 0; padding: 0; }
  html, body {
    width: 1200px; height: 952px; overflow: hidden;
    background: var(--stage);
    font-family: "Montserrat", sans-serif;
  }
  .canvas { position: relative; width: 1200px; height: 952px; }

  .card {
    position: absolute; left: 290px;
    width: 620px; height: 354px;
    border-radius: 22px; overflow: hidden;
    box-shadow: 0 14px 30px rgba(0,0,0,.35);
  }
  .card--front { top: 84px; background: var(--card-white); }
  .card--back  { top: 514px; background: var(--slate); }

  /* front */
  .brand-name {
    position: absolute; left: 150px; top: 30px;
    font-weight: 800; font-size: 40px; line-height: 1; letter-spacing: 3px; color: var(--ink);
  }
  .address-line {
    position: absolute; left: 30px; top: 100px; display: flex; gap: 10px;
    font-size: 12px; line-height: 1.35; color: var(--muted);
  }
  .address-line svg { flex: none; width: 15px; height: 15px; }

  .contact-band { position: absolute; left: 0; top: 142px; width: 330px; height: 150px; }
  .contact-list {
    position: absolute; left: 30px; top: 156px; list-style: none;
    color: #fff; font-size: 12px; line-height: 1.35;
  }
  .contact-list li { display: flex; align-items: center; gap: 10px; margin-bottom: 8px; }
  .contact-list svg { flex: none; width: 15px; height: 15px; }

  .person {
    position: absolute; right: 40px; top: 140px; text-align: right;
    color: var(--ink);
  }
  .person-name { font-size: 20px; font-weight: 400; letter-spacing: .5px; line-height: 1.2; }
  .person-name strong { font-weight: 800; }
  .person-role {
    display: inline-block; margin-top: 4px; padding-bottom: 6px;
    font-size: 14px; color: var(--muted);
    border-bottom: 2px solid var(--ink);
  }
  .circuit-faint {
    position: absolute; left: 335px; top: 215px; width: 250px; height: 125px;
    background: radial-gradient(ellipse at 40% 60%, var(--trace-mid), var(--trace-faint) 55%, var(--card-white) 85%);
  }

  /* back */
  .back-name {
    position: absolute; left: 46px; top: 66px;
    font-weight: 800; font-size: 62px; line-height: 1; letter-spacing: 4px; color: #fff;
  }
  .circuit-bright {
    position: absolute; left: 300px; top: 40px; width: 290px; height: 290px;
    border-radius: 14px;
    background: radial-gradient(ellipse at 45% 55%, #8c959b, var(--slate-light) 60%, var(--slate) 90%);
  }
</style>
</head>
<body>
<main class="canvas">

  <section class="card card--front" aria-label="Card front">
    <div class="brand-name">VORL</div>

    <div class="address-line">
      <svg viewBox="0 0 16 16"><rect width="16" height="16" rx="3" fill="#37424a"/><path d="M8 3a3 3 0 0 0-3 3c0 2.3 3 6 3 6s3-3.7 3-6a3 3 0 0 0-3-3zm0 4.2A1.2 1.2 0 1 1 8 4.8a1.2 1.2 0 0 1 0 2.4z" fill="#fff"/></svg>
      <span>42-44 Harbour Lane Westmere<br>NSW 2150 Australia</span>
    </div>

    <svg class="contact-band" viewBox="0 0 330 150" aria-hidden="true">
      <path d="M0 0 H300 V60 L315 75 V130 L300 145 H0 Z" fill="#37424a"/>
      <circle cx="300" cy="142" r="5" fill="#fff" stroke="#37424a" stroke-width="2"/>
    </svg>

    <ul class="contact-list">
      <li>
        <svg viewBox="0 0 16 16"><rect width="16" height="16" rx="3" fill="#fff"/><path d="M5 3.5l2 2-1 1.3a6 6 0 0 0 3.2 3.2l1.3-1 2 2-1.3 1.5C7.8 12.2 3.8 8.2 3.5 4.8z" fill="#37424a"/></svg>
        <span>+00 987 654 32</span>
      </li>
      <li>
        <svg viewBox="0 0 16 16"><rect width="16" height="16" rx="3" fill="#fff"/><rect x="3" y="4.5" width="10" height="7" fill="none" stroke="#37424a" stroke-width="1.4"/><path d="M3 4.5l5 4 5-4" fill="none" stroke="#37424a" stroke-width="1.4"/></svg>
        <span>admin@vorl.com.au</span>
      </li>
      <li>
        <svg viewBox="0 0 16 16"><rect width="16" height="16" rx="3" fill="#fff"/><path d="M4 12L8 3l4 9-4-2z" fill="#37424a"/></svg>
        <span>www.vorl.com.au</span>
      </li>
    </ul>

    <div class="person">
      <div class="person-name">DANIEL M. <strong>HARTLEY</strong></div>
      <div class="person-role">Managing Director</div>
    </div>

    <div class="circuit-faint" role="img" aria-label="Faint circuit-tree decoration in light grey"></div>
  </section>

  <section class="card card--back" aria-label="Card back">
    <div class="back-name">VORL</div>
    <div class="circuit-bright" role="img" aria-label="Light grey circuit-tree decoration on slate"></div>
  </section>

</main>
</body>
</html>
```